Luxury travel agency needs a website design

We are a travel agency specializing in booking luxury vacations. We specialize in Hawaii, Europe and Caribbean, but will do all vacations. I want a very classy website design which would attract luxury clients. The company name is "Harbors and Hammocks Travel Agency". Would love the web design to go with the color scheme of the logo. Hex codes included in files. Logo is attached. Would also love more Grey in the website. I want it very elegant

Coding

Coded - Design and coding required

Font styles to use
Sans Serif
Decorative

Requirements
Must have
• - Consultation Tab or a page where the client can fill out a short form about what vacation that they would want to book. I want this info to be sent to me in order for me to contact them.
- Somewhere with my contact info "email: marla@harborsandhammockstravel.example and phone number"
- Social media links
- About section "Marla Dovering - Agency Owner (picture provided)
Marla has been traveling full time for the passed two years and has been very passionate about travel from a young age. Marla is dedicated to working closely with clients to book their dream vacation.
Marla's specializations include honeymoons and anniversaries focusing on travel in Europe, Hawaii and all inclusive resorts in the Caribbean.

```html
<!DOCTYPE html>
<html lang="en">
<head>
<meta charset="utf-8">
<title>Harbors &amp; Hammocks Travel Agency</title>
<link href="https://fonts.googleapis.com/css2?family=Poppins:wght@400;500;600&family=Arimo:wght@400;700&display=swap" rel="stylesheet">
<style>
:root{
  --orange:#f08a4b;
  --navy:#1c2a3a;
  --ink:#1e1e1e;
  --grey:#e6e6e6;
  --muted:#555;
  --white:#fff;
}
*{box-sizing:border-box;margin:0;padding:0}
html,body{width:1200px;height:2861px;overflow:hidden;background:var(--white)}
body{position:relative;font-family:'Poppins',sans-serif;color:var(--ink)}
.abs{position:absolute}
.topbar{left:0;top:0;width:1200px;height:28px;background:var(--navy);color:#fff;font-size:11px}
.topbar .info{position:absolute;left:146px;top:7px;display:flex;gap:14px;align-items:center}
.topbar .social{position:absolute;right:146px;top:8px;display:flex;gap:10px}
.topbar .social span{width:11px;height:11px;border-radius:50%;border:1.5px solid #fff;display:block}
.header{left:0;top:28px;width:1200px;height:99px;background:#fff}
.brand{position:absolute;left:146px;top:32px;display:flex;align-items:center;gap:8px;font-weight:600;font-size:18px;color:var(--ink)}
.brand i{width:14px;height:14px;border-radius:50%;background:var(--orange);display:block}
.nav{position:absolute;right:146px;top:34px;display:flex;align-items:center;gap:33px;font-size:12.5px}
.nav .active{color:var(--orange)}
.btn{background:var(--orange);color:#fff;border-radius:3px;display:inline-flex;align-items:center;justify-content:center}
.nav .btn{width:110px;height:28px}
.hero{left:0;top:127px;width:1200px;height:547px;background:linear-gradient(180deg,#4a5d6d 0%,#c98a45 35%,#7c6a47 55%,#466a2c 80%,#3b5626 100%)}
.hero-text{left:0;top:288px;width:1200px;text-align:center;color:#fff;font-family:'Arimo',sans-serif;text-shadow:0 2px 6px rgba(0,0,0,.35)}
.hero-text .pre{font-size:26px}
.hero-text h1{font-size:44px;font-weight:700;margin-top:2px}
.hero-text p{font-size:24px;line-height:31px;margin-top:14px}
.booking{left:146px;top:612px;width:907px;height:129px;background:#fff;border-radius:6px;box-shadow:0 3px 10px rgba(0,0,0,.12);overflow:hidden}
.booking .bar{height:39px;background:var(--orange);color:#fff;display:flex;justify-content:space-between;align-items:center;padding:0 19px;font-size:15px}
.booking .bar b{font-weight:600;font-size:13px}
.fields{position:absolute;top:64px;left:19px;display:flex;gap:10px}
.field{height:34px;border:1px solid #c9c9c9;border-radius:2px;font-size:11px;color:var(--orange);padding:0 12px;display:flex;align-items:center;justify-content:space-between}
.fields .btn{width:123px;height:34px;font-size:12px}
.sec-title{font-size:26px;display:flex;align-items:center;gap:20px;left:148px;width:905px}
.sec-title::after{content:"";flex:1;height:1px;background:var(--grey)}
.ring{border-radius:50%;background:var(--grey)}
.photo{border-radius:50%;border:5px solid #fff}
.owner{left:528px;top:880px;width:428px}
.owner h3{font-weight:500;font-size:19px}
.owner .role{color:var(--orange);font-size:14px;margin-top:2px}
.owner p{font-size:13.3px;line-height:22px;text-align:justify;margin-top:16px;color:#222}
.owner p+p{margin-top:0}
.banner{left:0;top:1166px;width:1200px;height:553px;background:linear-gradient(180deg,#5f7c95 0%,#3e6f5a 22%,#1f6b86 45%,#2a8f94 62%,#2f6b2e 85%,#335a23 100%)}
.banner-text{left:0;top:1360px;width:1200px;text-align:center;color:#fff;text-shadow:0 2px 6px rgba(0,0,0,.4)}
.banner-text h2{font-family:'Arimo',sans-serif;font-size:58px;font-weight:700}
.banner-text p{font-size:15px;margin-top:4px}
.banner-btns{left:0;top:1467px;width:1200px;display:flex;justify-content:center;gap:10px}
.banner-btns span{width:122px;height:33px;font-size:12px;display:flex;align-items:center;justify-content:center;color:#fff;border-radius:2px}
.banner-btns .ghost{border:1.5px solid #fff}
.landmarks{left:0;top:2240px;width:1200px;height:432px;background:linear-gradient(180deg,rgba(255,255,255,0) 0%,#e4e7eb 20%,#b9a78d 48%,#8fae3e 74%,#6f9a23 100%)}
.dest{width:270px;text-align:center;z-index:2}
.dest h4{font-weight:500;font-size:19px}
.dest p{font-size:11px;line-height:17px;margin-top:8px;color:#333}
.dest .btn{width:98px;height:26px;font-size:9px;margin-top:12px}
.call{left:374px;top:2533px;width:457px;height:40px;border-radius:20px;background:var(--orange);color:#fff;font-family:'Arimo',sans-serif;font-weight:700;font-size:28px;display:flex;align-items:center;justify-content:center}
.footer{left:0;top:2670px;width:1200px;height:165px;background:#fff}
.foot-brand{left:0;top:2735px;width:1200px;text-align:center;font-weight:600;font-size:20px}
.foot-nav{left:0;top:2800px;width:1200px;display:flex;justify-content:center;gap:33px;font-size:12px}
.foot-nav .active{color:var(--orange)}
.copy{left:0;top:2835px;width:1200px;height:26px;background:var(--orange);color:#fff;font-size:10px;display:flex;align-items:center;justify-content:center}
</style>
</head>
<body>
<div class="abs topbar">
  <div class="info">
    <span>✉ marla@harborsandhammockstravel.example</span>
    <span><b style="font-weight:500">☎ Marla Dovering :</b> 2314-555-0148</span>
  </div>
  <div class="social" aria-label="Social media links"><span></span><span></span><span></span></div>
</div>

<header class="abs header">
  <div class="brand"><i></i>Harbors &amp; Hammocks</div>
  <nav class="nav">
    <span class="active">Home</span><span>About</span><span>Destination</span><span>Contact</span>
    <span class="btn">Consultation</span>
  </nav>
</header>

<div class="abs hero" role="img" aria-label="Photo of a tropical coastline at sunset with mossy rocks and waves"></div>
<div class="abs hero-text">
  <div class="pre">WE ARE A TRAVEL AGENCY SPECIALIZING IN</div>
  <h1>BOOKING LUXURY VACATIONS</h1>
  <p>We specialize in Hawaii, Europe and Caribbean<br>but will do all vacations.</p>
</div>

<form class="abs booking">
  <div class="bar"><span>REQUEST A BOOKING</span><b>CALL 1234-1234-1234 OR FILL OUT THE FORM BELOW</b></div>
  <div class="fields">
    <div class="field" style="width:139px">Your Name</div>
    <div class="field" style="width:147px">Contact Number</div>
    <div class="field" style="width:168px">Email Address</div>
    <div class="field" style="width:121px">Destination <span style="color:#999">⌄</span></div>
    <div class="field" style="width:121px">Date <span style="color:#999">⌄</span></div>
    <span class="btn">Submith</span>
  </div>
</form>

<h2 class="abs sec-title" style="top:778px;font-weight:400">About Us</h2>
<div class="abs ring" style="left:240px;top:856px;width:237px;height:237px"></div>
<div class="abs photo" role="img" aria-label="Portrait photo of the agency owner" style="left:228px;top:876px;width:230px;height:230px;background:linear-gradient(135deg,#7a5a44,#c59a7a 55%,#4aa7b8)"></div>
<div class="abs owner">
  <h3>Marla Dovering</h3>
  <div class="role">Agency Owner</div>
  <p>Marla has been traveling full time for the passed two years and has been very passionate about travel from a young age. Marla is dedicated to working closely with clients to book their dream vacation.</p>
  <p>Marla's specializations include honeymoons and anniversaries focusing on travel in Europe, Hawaii and all inclusive resorts in the Caribbean.</p>
</div>

<div class="abs banner" role="img" aria-label="Aerial photo of a Caribbean bay with green hills and sailboats"></div>
<div class="abs banner-text">
  <h2>Magnificent Caribbean Island</h2>
  <p>Recognizable, Lovely, Passionate and forever yours...</p>
</div>
<div class="abs banner-btns"><span class="ghost">Discover</span><span class="btn">Book Your Trip</span></div>

<h2 class="abs sec-title" style="top:1791px;font-weight:400">Destination</h2>

<div class="abs landmarks" role="img" aria-label="Illustrated collage of European landmarks and mountains above green grass"></div>

<div class="abs ring" style="left:163px;top:1887px;width:237px;height:237px"></div>
<div class="abs photo" role="img" aria-label="Photo of a Hawaiian black sand beach with cliffs" style="left:152px;top:1907px;width:230px;height:230px;background:linear-gradient(180deg,#8ea8bd,#6a6040 50%,#2e3a44)"></div>
<div class="abs ring" style="left:493px;top:1887px;width:237px;height:237px"></div>
<div class="abs photo" role="img" aria-label="Photo of a turquoise Caribbean cove" style="left:482px;top:1907px;width:230px;height:230px;background:linear-gradient(180deg,#4d8fd6,#57c9d6 50%,#3c7a2a)"></div>
<div class="abs ring" style="left:815px;top:1887px;width:237px;height:237px"></div>
<div class="abs photo" role="img" aria-label="Photo of a Paris skyline with an iron tower" style="left:804px;top:1907px;width:230px;height:230px;background:linear-gradient(180deg,#8fb4d8,#d7dde3 55%,#a58a6a)"></div>

<div class="abs dest" style="left:136px;top:2153px"><h4>Hawaii</h4><p>Lorem ipsum dolor sit amet, consectetur adip-isicing elit, sed do eiusmod tempor incididunt ut labore et dolore magna aliqua.</p><span class="btn">Book Your Trip</span></div>
<div class="abs dest" style="left:466px;top:2153px"><h4>Caribbean</h4><p>Lorem ipsum dolor sit amet, consectetur adip-isicing elit, sed do eiusmod tempor incididunt ut labore et dolore magna aliqua.</p><span class="btn">Book Your Trip</span></div>
<div class="abs dest" style="left:788px;top:2153px"><h4>Europe</h4><p>Lorem ipsum dolor sit amet, consectetur adip-isicing elit, sed do eiusmod tempor incididunt ut labore et dolore magna aliqua.</p><span class="btn">Book Your Trip</span></div>

<div class="abs call">CALL TODAY : 1234-1234-1234</div>

<svg class="abs" style="left:0;top:2620px" width="1200" height="52" viewBox="0 0 1200 52"><path d="M470 52 Q600 -40 730 52 Z" fill="#fff"/></svg>
<footer class="abs footer"></footer>
<div class="abs foot-brand"><span style="display:inline-block;width:14px;height:14px;border-radius:50%;background:var(--orange);margin-right:8px;vertical-align:middle"></span>Harbors &amp; Hammocks</div>
<nav class="abs foot-nav"><span class="active">Home</span><span>About</span><span>Destination</span><span>Contact</span><span>Book your Travel</span></nav>
<div class="abs copy">Copyright © 2021 Harbors &amp; Hammocks. All Rights Reserved</div>
</body>
</html>
```